ARC VOLLEY Business Card Project

I'd like to request a business card design for the new company I've launched.
The name of the company is "ARC VOLLEY" an indoor unmanned tennis practice facility.
We would like to see designs that use our brand identity color in the logo I've attached.
We hope to get the design with modern, luxurious and elegant tone and manner.
We hope the logo should not be too big.

Business card must have elements as below:
- Logo (One of the logos I've attached)
- Name (In Korean Text) : 박 서 윤
- Title (In Korean Text) : 대표
- Phone Number : 010-8472-3916
- Email Address : seoyun.park@arcvolley-example.co.kr
- Website : www.arcvolley-example.co.kr
- Instagram : arcvolley
- Address (In Korean text) : 경기도 용인시 수지구 풍덕천로 456 미래타워 5층 501호, 502호

Target Market(s)

Tennis amateurs in 20 to 40s

Industry/Entity Type

Sports, Hobby

Contact Information for Business Card

- Logo (One of the logos I've attached) - Name (In Korean Text) : 박 서 윤 - Title (In Korean Text) : 대표 - Phone Number : 010-8472-3916 - Email Address : seoyun.park@arcvolley-example.co.kr - Website : www.arcvolley-example.co.kr - Instagram : arcvolley - Address (In Korean text) : 경기도 용인시 수지구 풍덕천로 456 미래타워 5층 501호, 502호

Font styles to use
Sans Serif

Requirements
Must have
• Double sided
Nice to have
• Logo with intaglio or relief embossing
Should not have
• Logo should not be too big.

```html
<!DOCTYPE html>
<html lang="ko">
<head>
<meta charset="utf-8">
<title>ARC VOLLEY Business Card</title>
<link href="https://fonts.googleapis.com/css2?family=Montserrat:wght@400;500;600&family=Noto+Sans+KR:wght@400;500&display=swap" rel="stylesheet">
<style>
  :root {
    --backdrop: #a7abac;
    --paper: #f5f4f0;
    --paper-back: #efeee9;
    --brand-green: #1f5230;
    --edge-green: #173d25;
    --name-navy: #2b3b6b;
    --title-red: #c61f2e;
    --ink-grey: #5a5c5e;
    --rule-grey: #7b7d80;
  }
  * { margin: 0; padding: 0; box-sizing: border-box; }
  html, body {
    width: 1200px;
    height: 794px;
    overflow: hidden;
    background: var(--backdrop);
  }
  .canvas {
    width: 1200px;
    height: 794px;
    display: flex;
    align-items: center;
    justify-content: center;
    gap: 40px;
  }
  .card {
    position: relative;
    width: 540px;
    height: 300px;
    background: var(--paper);
    border-bottom: 4px solid var(--edge-green);
    box-shadow: 0 10px 24px rgba(0,0,0,0.18);
  }
  .card--back { background: var(--paper-back); }

  .brand-name {
    font-family: "Montserrat", sans-serif;
    font-weight: 600;
    color: var(--brand-green);
    letter-spacing: 0.06em;
    white-space: nowrap;
  }

  /* front */
  .front-logo {
    position: absolute;
    left: 40px;
    top: 134px;
    font-size: 22px;
  }
  .divider {
    position: absolute;
    left: 250px;
    top: 78px;
    width: 1px;
    height: 140px;
    background: var(--rule-grey);
  }
  .contact {
    position: absolute;
    left: 268px;
    top: 76px;
    width: 252px;
  }
  .person-name {
    font-family: "Noto Sans KR", sans-serif;
    font-weight: 400;
    font-size: 19px;
    color: var(--name-navy);
    letter-spacing: 0.25em;
    line-height: 1.1;
  }
  .person-title {
    font-family: "Noto Sans KR", sans-serif;
    font-weight: 500;
    font-size: 11px;
    color: var(--title-red);
    margin-top: 1px;
  }
  .contact-line {
    font-family: "Montserrat", sans-serif;
    font-size: 10px;
    color: var(--ink-grey);
    line-height: 1.5;
    white-space: nowrap;
  }
  .contact-line--first { margin-top: 9px; }
  .contact-label {
    display: inline-block;
    width: 14px;
    font-weight: 600;
    color: var(--brand-green);
  }
  .contact-address {
    font-family: "Noto Sans KR", sans-serif;
    font-size: 9.5px;
    color: var(--ink-grey);
    line-height: 1.5;
    margin-top: 2px;
  }

  /* back */
  .back-logo {
    position: absolute;
    left: 0;
    right: 0;
    top: 50%;
    transform: translateY(-50%);
    text-align: center;
    font-size: 40px;
  }
</style>
</head>
<body>
  <main class="canvas">
    <section class="card card--front" aria-label="Business card front">
      <div class="brand-name front-logo">ARC VOLLEY</div>
      <div class="divider"></div>
      <div class="contact">
        <p class="person-name">박 서 윤</p>
        <p class="person-title">대표</p>
        <p class="contact-line contact-line--first"><span class="contact-label">T</span>010-8472-3916</p>
        <p class="contact-line"><span class="contact-label">E</span>seoyun.park@arcvolley-example.co.kr</p>
        <p class="contact-line"><span class="contact-label">W</span>www.arcvolley-example.co.kr</p>
        <p class="contact-line"><span class="contact-label">I</span>@arcvolley</p>
        <p class="contact-address">경기도 용인시 수지구 풍덕천로 456<br>미래타워 5층 501호, 502호</p>
      </div>
    </section>
    <section class="card card--back" aria-label="Business card back">
      <div class="brand-name back-logo">ARC VOLLEY</div>
    </section>
  </main>
</body>
</html>
```